Brambury Logistics

Create a modern, simple, Elegant business card design for my business.

Services: Tamo Trucks, Transport, Contract Logistics,

Industry/Entity Type

Business

Contact Information for Business Card

Include all details same as old card plus new website address: www.bramburylogistics.com.au

Requirements
Must have
• Similar colors to Logo.

```html
<!DOCTYPE html>
<html lang="en">
<head>
<meta charset="utf-8">
<title>Brambury Logistics — Business Card</title>
<link rel="stylesheet" href="https://fonts.googleapis.com/css2?family=Cabin:wght@400;600&family=Cormorant+Garamond:ital,wght@1,600&display=swap">
<style>
  :root {
    --backdrop: #879995;
    --navy: #161a2c;
    --royal: #04338f;
    --sky: #47cdf7;
    --paper: #fbfbfd;
    --muted: #4b5b78;
    --ink: #111111;
    --brand-grey: #b9c2c8;
  }
  * { margin: 0; padding: 0; box-sizing: border-box; }
  html, body { width: 980px; height: 1200px; overflow: hidden; }
  body {
    background: var(--backdrop);
    position: relative;
    font-family: "Cabin", Arial, sans-serif;
  }
  .card { position: absolute; width: 713px; overflow: hidden; }

  /* Front */
  .card--front { left: 126px; top: 132px; height: 410px; background: var(--navy); }
  .brand {
    position: absolute; left: 0; right: 0; text-align: center;
    color: var(--brand-grey); font-weight: 600; letter-spacing: 1px;
  }
  .card--front .brand { top: 150px; font-size: 46px; }
  .services {
    position: absolute; top: 302px; left: 0; right: 0;
    display: flex; justify-content: center; align-items: center; gap: 18px;
    color: var(--muted); font-size: 17px;
  }
  .services .divider { width: 3px; height: 11px; background: #2e8be6; }
  .front-band { position: absolute; left: 0; right: 0; bottom: 0; height: 40px; background: var(--royal); }

  /* Back */
  .card--back { left: 120px; top: 711px; height: 413px; background: var(--navy); }
  .back-panel { position: absolute; inset: 0; }
  .card--back .brand { top: 172px; left: 30px; right: auto; width: 330px; font-size: 30px; }
  .name-ribbon {
    position: absolute; left: 414px; top: 91px; width: 299px; height: 43px;
    background: var(--sky);
    font-family: "Cormorant Garamond", Georgia, serif; font-style: italic; font-weight: 600;
    font-size: 28px; color: var(--ink); text-align: center; line-height: 43px;
  }
  .contacts { position: absolute; left: 432px; top: 202px; list-style: none; }
  .contact { display: flex; align-items: center; height: 40px; margin-bottom: 17px; color: var(--ink); }
  .contact__icon {
    width: 38px; height: 38px; border-radius: 50%; background: var(--royal);
    display: flex; align-items: center; justify-content: center; margin-right: 14px; flex: none;
  }
  .contact--phone { font-size: 22px; }
  .contact--email, .contact--web { font-size: 15px; }
</style>
</head>
<body>

<section class="card card--front">
  <div class="brand">Brambury Logistics</div>
  <p class="services">
    <span>Tamo Trucks</span><span class="divider"></span>
    <span>Transport</span><span class="divider"></span>
    <span>Contract Logistics</span>
  </p>
  <div class="front-band"></div>
</section>

<section class="card card--back">
  <svg class="back-panel" width="713" height="413" viewBox="0 0 713 413">
    <polygon points="509,0 713,0 713,413 358,413" fill="var(--paper)"/>
    <polygon points="414,134 456,134 436,163" fill="var(--royal)"/>
  </svg>
  <div class="brand">Brambury Logistics</div>
  <div class="name-ribbon">Name</div>
  <ul class="contacts">
    <li class="contact contact--phone">
      <span class="contact__icon">
        <svg width="20" height="20" viewBox="0 0 24 24"><path fill="#fff" d="M6.6 10.8a15 15 0 0 0 6.6 6.6l2.2-2.2c.3-.3.7-.4 1-.2 1.1.4 2.3.6 3.6.6.6 0 1 .4 1 1V20c0 .6-.4 1-1 1A17 17 0 0 1 3 4c0-.6.4-1 1-1h3.5c.6 0 1 .4 1 1 0 1.3.2 2.5.6 3.6.1.3 0 .7-.2 1z"/></svg>
      </span>0400 555 318
    </li>
    <li class="contact contact--email">
      <span class="contact__icon">
        <svg width="20" height="20" viewBox="0 0 24 24" fill="none" stroke="#fff" stroke-width="1.4"><rect x="3" y="6" width="18" height="13"/><path d="M3 6l9 7 9-7"/></svg>
      </span>Reno@bramburylogistics.com.au
    </li>
    <li class="contact contact--web">
      <span class="contact__icon">
        <svg width="22" height="22" viewBox="0 0 24 24" fill="none" stroke="#fff" stroke-width="1.2"><circle cx="12" cy="12" r="9"/><ellipse cx="12" cy="12" rx="4" ry="9"/><path d="M3 12h18M5 7h14M5 17h14"/></svg>
      </span>www.bramburylogistics.com.au
    </li>
  </ul>
</section>

</body>
</html>
```